Retail Jewelry Business Card Design Project

We are in need of a new business card design for a retail jewelry store. This store is in the business of fine jewelry including but not specific to bridal jewelry, diamonds, designer jewelry and watches.

This store has been in business for 20 years but continues to strive for a modern professional appeal. The main colors use for this business are a royal blue, white and silver.

Target Market(s)

Target market is ages 18-50

Industry/Entity Type

Jewelry

Requirements
Must have
• Sales Person Name
Sales Person Email Address

Store Address
Store Phone
Website

Standard business card size. No odd shapes or sizes.
Nice to have
• Overall modern feel for card.

We have thought that a design with a nice feature of the logo on the back of the card would be nice but open to ideas.
Should not have
• No specific images of jewelry should be used.

```html
<!DOCTYPE html>
<html lang="en">
<head>
<meta charset="utf-8">
<title>Marcus Hale Fine Jewelry – Business Card</title>
<link rel="stylesheet" href="https://fonts.googleapis.com/css2?family=Montserrat:wght@400;500&family=Crimson+Pro:ital,wght@1,400&display=swap">
<style>
  :root {
    --royal-blue: #2e3192;
    --silver-line: #7d7fbf;
    --card-white: #ffffff;
    --page-bg: #ffffff;
    --shadow: rgba(0, 0, 0, 0.14);
  }
  html, body {
    margin: 0;
    padding: 0;
    width: 980px;
    height: 1200px;
    overflow: hidden;
    background: var(--page-bg);
  }
  .sheet {
    position: relative;
    width: 980px;
    height: 1200px;
  }
  .card {
    position: absolute;
    left: 153px;
    width: 683px;
    height: 390px;
    box-shadow: 0 3px 10px var(--shadow);
    box-sizing: border-box;
  }
  .card-front {
    top: 147px;
    background: var(--card-white);
    display: flex;
    flex-direction: column;
    align-items: center;
    justify-content: center;
  }
  .brand-name,
  .brand-line {
    font-family: "Montserrat", sans-serif;
    font-weight: 500;
    color: var(--royal-blue);
    text-transform: uppercase;
    margin: 0;
    line-height: 1;
  }
  .brand-name {
    font-size: 50px;
    letter-spacing: 3px;
    margin-top: -14px;
  }
  .brand-line {
    font-size: 22px;
    letter-spacing: 6px;
    margin-top: 18px;
  }
  .card-back {
    top: 674px;
    background: var(--royal-blue);
    color: var(--card-white);
    text-align: center;
  }
  .person-name {
    position: absolute;
    top: 116px;
    left: 0;
    right: 0;
    margin: 0;
    font-family: "Montserrat", sans-serif;
    font-weight: 500;
    font-size: 29px;
    letter-spacing: 1.5px;
    text-transform: uppercase;
    line-height: 1;
  }
  .person-email {
    position: absolute;
    top: 153px;
    left: 0;
    right: 0;
    margin: 0;
    font-family: "Montserrat", sans-serif;
    font-weight: 400;
    font-size: 24px;
    line-height: 1;
  }
  .divider {
    position: absolute;
    top: 289px;
    left: 124px;
    width: 436px;
    height: 3px;
    background: var(--silver-line);
  }
  .store-details {
    position: absolute;
    top: 306px;
    left: 0;
    right: 0;
    margin: 0;
    font-family: "Crimson Pro", serif;
    font-style: italic;
    font-size: 19px;
    line-height: 23px;
  }
  .store-details span + span {
    margin-left: 18px;
  }
</style>
</head>
<body>
  <main class="sheet">
    <section class="card card-front" aria-label="Card front">
      <p class="brand-name">Marcus Hale</p>
      <p class="brand-line">Fine Jewelry</p>
    </section>

    <section class="card card-back" aria-label="Card back">
      <h1 class="person-name">Marcus Hale Brennan</h1>
      <p class="person-email">marcus@marcushalejewelry.com</p>
      <div class="divider"></div>
      <address class="store-details">
        <div><span>2270 Linden Avenue</span><span>Bayport, FL 32599</span></div>
        <div><span>(555)301-4482</span><span>www.marcushalejewelry.com</span></div>
      </address>
    </section>
  </main>
</body>
</html>
```